Tradeshow Exhibit Background Design

Looking to make improvements on my tradeshow exhibit backdrop. I created the current design myself, and I'm not 100% happy with it. Because its a big investment, I want it to be perfect.
For context:
- The booth will be used in multiple configurations (20 ft, 10 ft, and 8 ft).
- The booth structure will include two panels that are 5' x 7.5', and one panel that is 8' x 8.5' (attached a photo of the set-up.)
- We plan on getting the double sided fabric printing so that we can use it in the various configurations (the 10' config will be the two 5' panels put together, and the 20' config will be all three.)
The design should be visually impactful from a distance but also clear and readable up close. It needs to align with our brand identity and effectively communicate what we do at a glance.
I've includes a photo example of the booth structure, my current design, as well as our company brand guidelines.

```html
<!DOCTYPE html>
<html lang="en">
<head>
<meta charset="utf-8">
<title>Stratapeak Tradeshow Exhibit</title>
<link href="https://fonts.googleapis.com/css2?family=Exo+2:wght@600;800&family=Open+Sans:wght@400;700&family=Titillium+Web:wght@600;700&display=swap" rel="stylesheet">
<style>
  :root {
    --backdrop: #e2e2e2;
    --ink-dark: #24343c;
    --brand-red: #d3272e;
    --body-grey: #4a4f54;
    --counter-grey: #737d86;
    --counter-edge: #cdb38a;
    --counter-text: #f3f3f3;
    --sky-top: #2f6f9e;
    --sky-light: #b9d6e6;
    --pit-mid: #4d7790;
    --pit-dark: #1f3a4d;
    --rock-dark: #13222e;
  }
  * { margin: 0; padding: 0; box-sizing: border-box; }
  html, body { width: 1200px; height: 849px; overflow: hidden; background: var(--backdrop); }
  .exhibit { position: relative; width: 1200px; height: 849px; }

  .side-panel {
    position: absolute; top: 307px; width: 238px; height: 358px;
    background: linear-gradient(180deg, var(--sky-top) 0%, var(--sky-light) 16%, var(--pit-mid) 30%, #6f97ad 48%, var(--pit-dark) 72%, var(--rock-dark) 100%);
  }
  .side-panel--left { left: 250px; }
  .side-panel--right { left: 732px; }

  .center-panel {
    position: absolute; left: 487px; top: 192px; width: 245px; height: 476px;
    background: linear-gradient(180deg, #fafafa, #e9e9e9);
    text-align: center;
  }
  .brand-name {
    position: absolute; left: 0; right: 0; top: 80px;
    font-family: "Exo 2", sans-serif; font-weight: 800; font-size: 22px; letter-spacing: 0.5px;
    color: var(--ink-dark);
  }
  .brand-dot { display: inline-block; width: 5px; height: 5px; border-radius: 50%; background: var(--brand-red); vertical-align: top; margin-left: 1px; margin-top: 2px; }
  .headline {
    position: absolute; left: 0; right: 0; top: 106px;
    font-family: "Titillium Web", sans-serif; font-weight: 700; font-size: 8.6px; line-height: 10.4px;
    letter-spacing: 0.2px; color: var(--brand-red);
  }
  .intro {
    position: absolute; left: 12px; right: 12px; top: 129px;
    font-family: "Open Sans", sans-serif; font-size: 5.3px; line-height: 7px; color: var(--body-grey);
  }
  .service { position: absolute; width: 74px; text-align: center; line-height: 0; }
  .service svg { display: block; margin: 0 auto; }
  .service-label {
    display: inline-block; margin-top: 3px; font-family: "Open Sans", sans-serif; font-weight: 700;
    font-size: 3.6px; line-height: 4px; color: var(--ink-dark);
    border-bottom: 0.6px solid var(--brand-red); padding-bottom: 0.5px;
  }
  .site-url {
    position: absolute; left: 0; right: 0; top: 308px;
    font-family: "Titillium Web", sans-serif; font-weight: 700; font-size: 8.4px; letter-spacing: 0.3px;
    color: var(--brand-red);
  }

  .counter {
    position: absolute; top: 509px; width: 196px; height: 190px;
    background: var(--counter-grey); border-top: 5px solid var(--counter-edge);
    text-align: center; color: var(--counter-text);
  }
  .counter--left { left: 199px; }
  .counter--right { left: 825px; }
  .counter-name { margin-top: 62px; font-family: "Exo 2", sans-serif; font-weight: 800; font-size: 22px; letter-spacing: 0.5px; }
  .counter-name .brand-dot { background: var(--counter-text); }
  .counter-url { margin-top: 4px; font-family: "Exo 2", sans-serif; font-weight: 600; font-size: 10px; letter-spacing: 0.3px; }
</style>
</head>
<body>
<main class="exhibit">
  <div class="side-panel side-panel--left" role="img" aria-label="Open-pit mine landscape with haul road, drill rigs and blue sky"></div>
  <div class="side-panel side-panel--right" role="img" aria-label="Open-pit mine landscape with haul road, drill rigs and blue sky"></div>

  <section class="center-panel">
    <div class="brand-name">STRATAPEAK<span class="brand-dot"></span></div>
    <h1 class="headline">COMPANIES THAT WORK WITH<br>STRATAPEAK ARE READY FOR THE FUTURE OF MINING.</h1>
    <p class="intro">We are mining professionals, with engineering and operational experience, and the global knowledge to partner with you to uncover your growth potential and implement a program to maximize your organization's success.</p>

    <svg width="0" height="0" style="position:absolute">
      <defs>
        <linearGradient id="hex-warm" x1="0" y1="0" x2="0" y2="1"><stop offset="0" stop-color="#c9c3b8"/><stop offset="1" stop-color="#5a5148"/></linearGradient>
        <linearGradient id="hex-cool" x1="0" y1="0" x2="0" y2="1"><stop offset="0" stop-color="#b8c8d8"/><stop offset="1" stop-color="#2d3d52"/></linearGradient>
        <linearGradient id="hex-site" x1="0" y1="0" x2="0" y2="1"><stop offset="0" stop-color="#9aa3a8"/><stop offset="1" stop-color="#c88a3a"/></linearGradient>
      </defs>
    </svg>

    <div class="service" style="left:8px;top:152px">
      <svg width="66" height="58" viewBox="0 0 66 58" role="img" aria-label="Audience attending a mining assessment presentation"><polygon points="16,0 50,0 66,29 50,58 16,58 0,29" fill="url(#hex-cool)"/></svg>
      <span class="service-label">COMPREHENSIVE<br>ASSESSMENTS</span>
    </div>
    <div class="service" style="left:86px;top:152px">
      <svg width="66" height="58" viewBox="0 0 66 58" role="img" aria-label="Yellow haul trucks at a mine site"><polygon points="16,0 50,0 66,29 50,58 16,58 0,29" fill="url(#hex-site)"/></svg>
      <span class="service-label">ADVANCED<br>DISPATCH PROGRAM</span>
    </div>
    <div class="service" style="left:164px;top:152px">
      <svg width="66" height="58" viewBox="0 0 66 58" role="img" aria-label="Workers in hard hats at a control monitor"><polygon points="16,0 50,0 66,29 50,58 16,58 0,29" fill="url(#hex-warm)"/></svg>
      <span class="service-label">MAINTENANCE<br>&amp; RELIABILITY</span>
    </div>
    <div class="service" style="left:8px;top:227px">
      <svg width="66" height="58" viewBox="0 0 66 58" role="img" aria-label="Mine crew in orange hard hats"><polygon points="16,0 50,0 66,29 50,58 16,58 0,29" fill="url(#hex-warm)"/></svg>
      <span class="service-label">OMS PERFORMANCE<br>MANAGEMENT PROGRAM</span>
    </div>
    <div class="service" style="left:86px;top:227px">
      <svg width="66" height="58" viewBox="0 0 66 58" role="img" aria-label="Workers in safety vests walking on site"><polygon points="16,0 50,0 66,29 50,58 16,58 0,29" fill="url(#hex-site)"/></svg>
      <span class="service-label">OMS LEAD</span>
    </div>
    <div class="service" style="left:164px;top:227px">
      <svg width="66" height="58" viewBox="0 0 66 58" role="img" aria-label="Operator at an integrated operations control room"><polygon points="16,0 50,0 66,29 50,58 16,58 0,29" fill="url(#hex-cool)"/></svg>
      <span class="service-label">INTEGRATED<br>OPERATIONS</span>
    </div>

    <div class="site-url">STRATAPEAKMINING.COM</div>
  </section>

  <section class="counter counter--left">
    <div class="counter-name">STRATAPEAK<span class="brand-dot"></span></div>
    <div class="counter-url">stratapeakmining.com</div>
  </section>
  <section class="counter counter--right">
    <div class="counter-name">STRATAPEAK<span class="brand-dot"></span></div>
    <div class="counter-url">stratapeakmining.com</div>
  </section>
</main>
</body>
</html>
```